Coffee roastery and coffee shop needs a packaging design

We need a packaging design for an our company we sell coffee beans for coffee shops . and we have a coffee shop . our company name is (VELLUM ROASTERY) we are based in UAE. We want a cup design for cold coffee and hot and coffee bag design and paper bag design. I uploaded our logo design.

```html
<!DOCTYPE html>
<html lang="en">
<head>
<meta charset="UTF-8">
<title>Vellum Roastery – Coffee Bag Label</title>
<link href="https://fonts.googleapis.com/css2?family=Michroma&family=Montserrat:wght@300;400&display=swap" rel="stylesheet">
<style>
  :root {
    --canvas: #ffffff;
    --band-red: #b3474a;
    --ink: #333333;
    --ink-soft: #555555;
    --label-light: #ffffff;
    --label-grey: #e4e5e7;
    --berry-red: #a8282d;
    --leaf-olive: #b7b07a;
    --bean-brown: #8b6e55;
  }
  * { margin: 0; padding: 0; box-sizing: border-box; }
  html, body { width: 1200px; height: 1200px; overflow: hidden; background: var(--canvas); }
  .canvas { position: relative; width: 1200px; height: 1200px; }

  .label {
    position: absolute; left: 155px; top: 80px; width: 890px; height: 1040px;
    background: linear-gradient(225deg, var(--label-grey) 0%, #f1f2f3 45%, var(--label-light) 100%);
    overflow: hidden;
  }
  .label__band {
    position: absolute; left: 0; top: 0; width: 207px; height: 100%;
    background: var(--band-red);
  }
  .band-brand {
    position: absolute; left: 0; width: 207px; top: 770px; text-align: center; color: #fff;
  }
  .band-brand__name { font-family: "Michroma", sans-serif; font-size: 11px; letter-spacing: 4px; padding-left: 4px; }
  .band-brand__sub { font-family: "Montserrat", sans-serif; font-weight: 300; font-size: 4px; letter-spacing: 4px; }

  .art { position: absolute; }
  .art--branch {
    left: 207px; top: 0; width: 293px; height: 206px;
    background: radial-gradient(ellipse at 60% 55%, rgba(168,40,45,0.28), rgba(183,176,122,0.18) 60%, transparent 80%);
  }
  .art--beans {
    left: 426px; top: 421px; width: 216px; height: 331px;
    background: radial-gradient(ellipse at 50% 45%, rgba(139,110,85,0.22), rgba(214,170,90,0.14) 60%, transparent 80%);
  }
  .art--leaf {
    left: 731px; top: 815px; width: 159px; height: 225px;
    background: radial-gradient(ellipse at 45% 55%, rgba(183,176,122,0.28), transparent 75%);
  }

  .brand { position: absolute; left: 207px; width: 683px; text-align: center; color: var(--ink); }
  .brand__dot {
    position: absolute; left: 548px; top: 250px; width: 60px; height: 60px; margin-left: -30px;
    border: 4px solid var(--ink); border-radius: 50%;
  }
  .brand--name { top: 333px; }
  .brand__name { font-family: "Michroma", sans-serif; font-size: 27px; letter-spacing: 9px; padding-left: 9px; line-height: 1; }
  .brand__sub { margin-top: 8px; font-family: "Montserrat", sans-serif; font-weight: 300; font-size: 11px; letter-spacing: 12px; padding-left: 12px; }

  .seal { position: absolute; left: 318px; top: 685px; width: 80px; text-align: center; }
  .seal__badge { width: 64px; height: 64px; margin: 0 auto; border-radius: 50%; border: 5px solid var(--ink); background: #fff; }
  .seal__origin { margin-top: 5px; margin-left: -30px; width: 140px; font-family: "Montserrat", sans-serif; font-size: 8.5px; color: var(--ink-soft); }

  .product { position: absolute; left: 420px; width: 270px; top: 776px; text-align: center; color: var(--ink); }
  .product__kind { font-family: "Montserrat", sans-serif; font-weight: 300; font-size: 16px; letter-spacing: 0.3px; }
  .product__name { font-family: "Michroma", sans-serif; font-size: 33px; letter-spacing: 6px; padding-left: 6px; line-height: 1.1; }

  .methods { position: absolute; top: 850px; left: 450px; width: 216px; display: flex; justify-content: space-between; }
  .method { width: 52px; text-align: center; }
  .method svg { display: block; margin: 0 auto; height: 26px; }
  .method__label { margin-top: 5px; font-family: "Montserrat", sans-serif; font-size: 8px; color: var(--ink-soft); }

  .weight { position: absolute; top: 930px; left: 420px; width: 270px; text-align: center;
    font-family: "Michroma", sans-serif; font-size: 16px; letter-spacing: 3px; color: var(--ink); }
</style>
</head>
<body>
<main class="canvas">
  <section class="label">
    <div class="label__band">
      <div class="band-brand">
        <div class="band-brand__name">VELLUM</div>
        <div class="band-brand__sub">ROASTERY</div>
      </div>
    </div>

    <div class="art art--branch" role="img" aria-label="Line drawing of a coffee branch with red coffee cherries"></div>

    <div class="brand__dot"></div>
    <div class="brand brand--name">
      <div class="brand__name">VELLUM</div>
      <div class="brand__sub">ROASTERY</div>
    </div>

    <div class="art art--beans" role="img" aria-label="Scattered coffee beans in red, green, brown and gold tones"></div>

    <div class="seal">
      <div class="seal__badge"></div>
      <div class="seal__origin">PRODUCED IN THE UAE</div>
    </div>

    <div class="product">
      <div class="product__kind">ROASTED AND GROUND</div>
      <div class="product__name">COFFEE</div>
    </div>

    <div class="methods">
      <div class="method">
        <svg viewBox="0 0 30 26" width="30"><path d="M3 6 H27 L18 18 H12 Z M10 21 H20" fill="none" stroke="#333" stroke-width="1.5"/></svg>
        <div class="method__label">FILTER</div>
      </div>
      <div class="method">
        <svg viewBox="0 0 40 26" width="40"><circle cx="8" cy="8" r="5" fill="none" stroke="#333" stroke-width="1.5"/><path d="M12 10 L37 22" stroke="#333" stroke-width="3.5" stroke-linecap="round"/></svg>
        <div class="method__label">ESPRESSO</div>
      </div>
      <div class="method">
        <svg viewBox="0 0 24 26" width="24"><rect x="6" y="7" width="12" height="17" fill="none" stroke="#333" stroke-width="1.5"/><path d="M12 1 V7 M9 3 H15 M18 11 H21 V20 H18 M9 10 V22 M12 10 V22 M15 10 V22" stroke="#333" stroke-width="1.2" fill="none"/></svg>
        <div class="method__label">PLUNGER</div>
      </div>
      <div class="method">
        <svg viewBox="0 0 24 26" width="24"><ellipse cx="8" cy="7" rx="4" ry="5.5" fill="#333"/><ellipse cx="8" cy="19" rx="4" ry="5.5" fill="#333"/><ellipse cx="18" cy="13" rx="4" ry="5.5" fill="#333"/></svg>
        <div class="method__label">BEANS</div>
      </div>
    </div>

    <div class="weight">400G</div>

    <div class="art art--leaf" role="img" aria-label="Outline drawing of a large leaf"></div>
  </section>
</main>
</body>
</html>
```